Korelith InsurTech Website Redesign - 10 Pages

Design a modern, professional website for Korelith, an AI-native cyber insurance platform serving SMBs.

DELIVERABLE: 10 pages (desktop + mobile mockups)
- Homepage (priority #1)
- 4 Platform pages (Cyber Insurance, Brokers, Underwriters, Policyholder)
- 3 Company pages (About Us, Team, Contact/Careers)
- 2 Risk pages (AI Risk, Cyber Risk)

DESIGN DIRECTION:
- Professional + innovative (insurance meets technology)
- Trust-building + modern aesthetic
- Reference: Brambury Insurance, Tidewick Insurance
- Use official brand colors (6-color palette provided)
- Avoid generic security clipart (padlocks, shields, magnifying glasses)
- Custom graphics, not AI-generated or stock imagery

CURRENT SITES FOR REFERENCE:
- www.korelith.ai
- https://a3c9124d.korelith-website.vorlapages.dev/

Full detailed brief with all content, page specifications, and brand guidelines attached as PDF (Korelith_PixelHarbor_Brief.pdf).

TARGET AUDIENCE: Insurance brokers (primary), SMB business owners (secondary)
KEY MESSAGE: "Cyber Insurance the Way It Should Be"

Additional brand assets available in Google Drive - link provided on request.

```html
<!DOCTYPE html>
<html lang="en">
<head>
<meta charset="utf-8">
<title>Korelith — Cyber Insurance the Way It Should Be</title>
<link rel="stylesheet" href="https://fonts.googleapis.com/css2?family=Poppins:wght@400;600;700&family=Inter:wght@400;500;600&display=swap">
<style>
  :root{
    --green:#a3fca4;
    --green-deep:#5fd86a;
    --ink:#1d1d1d;
    --text:#3a3a3a;
    --muted:#6b6b6b;
    --black:#000;
    --footer:#232323;
    --footer-line:#3d3d3d;
    --white:#fff;
  }
  *{margin:0;padding:0;box-sizing:border-box}
  html,body{width:1200px;height:2659px;overflow:hidden;background:var(--white)}
  body{font-family:'Inter',sans-serif;color:var(--ink);position:relative}

  /* Hero */
  .hero{position:absolute;left:0;top:0;width:1200px;height:640px;
    background:radial-gradient(ellipse at 35% 30%,#fafafa 0%,#f1f1f1 60%,#ebebeb 100%)}
  .hero-visual{position:absolute;left:470px;top:0;width:730px;height:640px;
    background:radial-gradient(ellipse 260px 330px at 60% 40%,rgba(40,40,40,.28) 0%,rgba(40,40,40,.10) 55%,rgba(0,0,0,0) 100%)}
  .nav{position:absolute;left:111px;top:0;width:977px;height:116px;background:var(--black);
    border-radius:0 0 14px 14px;display:flex;align-items:center;padding:0 33px}
  .brand{font-family:'Poppins',sans-serif;font-weight:600;font-size:22px;color:var(--green);display:flex;align-items:center;gap:8px}
  .brand-dot{width:12px;height:12px;border-radius:50%;background:var(--green)}
  .nav-links{display:flex;gap:37px;margin-left:178px;list-style:none}
  .nav-links a{color:var(--white);text-decoration:none;font-weight:600;font-size:15px}
  .nav-links a.active{color:var(--green)}
  .btn{display:inline-block;background:var(--green);color:var(--ink);font-weight:600;font-size:14px;
    text-decoration:none;border-radius:6px}
  .nav .btn{margin-left:auto;padding:13px 24px}
  .hero-title{position:absolute;left:143px;top:272px;font-family:'Poppins',sans-serif;font-weight:700;font-size:44px;line-height:52px;color:var(--black)}
  .hero-sub{position:absolute;left:143px;top:385px;font-family:'Poppins',sans-serif;font-weight:600;font-size:20px;line-height:28px;color:#2b2b2b}
  .hero .cta{position:absolute;left:143px;top:453px;padding:13px 25px}

  /* Different */
  .different{position:absolute;left:0;top:640px;width:1200px;height:470px;
    background:radial-gradient(circle at 1050px 140px,#ecfdec 0%,rgba(255,255,255,0) 380px)}
  .section-title{text-align:center;font-family:'Poppins',sans-serif;font-size:40px;line-height:52px;font-weight:400;color:var(--ink)}
  .section-title b{font-weight:700}
  .different .section-title{position:absolute;left:0;right:0;top:78px}
  .feature{position:absolute;top:168px;width:266px}
  .feature-num{height:68px;overflow:hidden;font-family:'Poppins',sans-serif;font-weight:700;font-size:112px;line-height:118px;
    background:linear-gradient(180deg,var(--green) 0%,rgba(163,252,164,.15) 80%);-webkit-background-clip:text;background-clip:text;color:transparent}
  .feature h3{font-weight:600;font-size:19px;line-height:28px;margin-top:8px}
  .feature p{font-size:14.5px;line-height:22.5px;color:var(--text);margin-top:12px}

  /* Lifecycle */
  .lifecycle{position:absolute;left:0;top:1110px;width:1200px;height:765px;overflow:hidden;
    background:linear-gradient(100deg,rgba(163,252,164,.18) 0%,rgba(255,255,255,0) 30%,rgba(255,255,255,0) 65%,#f4f4f4 100%)}
  .lifecycle .section-title{position:absolute;left:0;right:0;top:40px}
  .ring{position:absolute;left:359px;top:413px;width:482px;height:482px;border-radius:50%;border:5px solid var(--green)}
  .core{position:absolute;left:407px;top:461px;width:386px;height:386px;border-radius:50%;background:var(--green);
    display:flex;justify-content:center;padding-top:150px;font-family:'Poppins',sans-serif;font-weight:600;font-size:34px;color:var(--ink)}
  .step{position:absolute;width:108px;height:108px;border-radius:50%;background:var(--green);
    display:flex;align-items:center;justify-content:center;font-family:'Poppins',sans-serif;font-weight:600;font-size:40px;color:var(--green-deep)}
  .step-text{position:absolute}
  .step-text h4{font-weight:600;font-size:19px;line-height:24px;color:var(--ink)}
  .step-text p{font-size:14.5px;line-height:22.5px;color:var(--muted);margin-top:6px}
  .right{text-align:right}
  .center{text-align:center}

  /* Integrations */
  .integrations{position:absolute;left:0;top:1875px;width:1200px;height:465px;
    background:linear-gradient(180deg,#fff 45%,#f4f4f4 100%)}
  .integrations .section-title{position:absolute;left:0;right:0;top:100px}
  .tool{position:absolute;top:247px;width:240px;text-align:center}
  .tool svg{display:block;margin:0 auto}
  .tool span{display:block;margin-top:18px;font-weight:500;font-size:20px;color:var(--ink)}

  /* Footer */
  .footer{position:absolute;left:0;top:2340px;width:1200px;height:319px;background:var(--footer);color:var(--white)}
  .footer-nav{position:absolute;left:0;right:0;top:64px;display:flex;justify-content:center;gap:43px;list-style:none}
  .footer-nav a{color:var(--white);text-decoration:none;font-weight:600;font-size:17px}
  .rule{position:absolute;left:143px;width:912px;height:1px;background:var(--footer-line)}
  .contact{position:absolute;top:130px;display:flex;gap:16px}
  .contact-icon{width:42px;height:42px;border-radius:50%;background:#333;display:flex;align-items:center;justify-content:center;flex:none}
  .contact small{display:block;font-weight:600;font-size:14px}
  .contact strong{display:block;font-weight:500;font-size:17px;line-height:22px;margin-top:2px}
  .copyright{position:absolute;left:0;right:0;top:246px;text-align:center;font-weight:500;font-size:14px}
</style>
</head>
<body>

<header class="hero">
  <div class="hero-visual" role="img" aria-label="Dotted particle funnel swirling down into a single point"></div>
  <nav class="nav">
    <div class="brand"><span class="brand-dot"></span>Korelith</div>
    <ul class="nav-links">
      <li><a class="active" href="#">Home</a></li>
      <li><a href="#">Platform</a></li>
      <li><a href="#">Cyber Risk</a></li>
      <li><a href="#">AI Risk</a></li>
      <li><a href="#">Company</a></li>
    </ul>
    <a class="btn" href="#">Contact Us</a>
  </nav>
  <h1 class="hero-title">Cyber Insurance the<br>Way It Should Be</h1>
  <p class="hero-sub">Evidence based, automation driven underwriting<br>for the AI era</p>
  <a class="btn cta" href="#">Contact Us</a>
</header>

<section class="different">
  <h2 class="section-title"><b>What Makes</b> Korelith Different</h2>
  <article class="feature" style="left:143px">
    <div class="feature-num">01</div>
    <h3>End to End Cyber Risk and Insurance Platform</h3>
    <p>The Korelith platform streamlines the entire policy lifecycle, incentivizes and empowers policyholders to actively reduce their risk, and elevates brokers as trusted advisors.</p>
  </article>
  <article class="feature" style="left:467px">
    <div class="feature-num">02</div>
    <h3>Proprietary Tools and Rapid Response</h3>
    <p>Advanced security tools and 24/7 incident response capabilities protect businesses before, during, and after cyber events.</p>
  </article>
  <article class="feature" style="left:791px">
    <div class="feature-num">03</div>
    <h3>Insurance DNA and Tech Execution</h3>
    <p>Founded by a team with deep expertise in cyber insurance and cybersecurity, we understand both the risk landscape and the insurance market.</p>
  </article>
</section>

<section class="lifecycle">
  <h2 class="section-title"><b>The Complete</b><br><b>Cyber</b> Insurance Lifecycle</h2>
  <div class="ring"></div>
  <div class="core">Korelith</div>

  <div class="step-text center" style="left:435px;top:168px;width:330px"><h4>IMPROVE</h4><p>Incentivize and guide policyholders to actively strengthen their cybersecurity through behavior rewards</p></div>
  <div class="step" style="left:546px;top:274px">03</div>

  <div class="step-text right" style="left:96px;top:357px;width:222px"><h4>ASSESS</h4><p>Dynamic scanning and read-only API integrations to continuously evaluate risk posture and inform underwriting</p></div>
  <div class="step" style="left:333px;top:351px">02</div>

  <div class="step" style="left:766px;top:351px">04</div>
  <div class="step-text" style="left:888px;top:357px;width:225px"><h4>REMEDIATE</h4><p>Expert post-breach services including forensics, restoration, and crisis management support</p></div>

  <div class="step-text right" style="left:52px;top:576px;width:166px"><h4>ENSURE</h4><p>Best in class cyber insurance coverage with comprehensive first and third party protections</p></div>
  <div class="step" style="left:234px;top:570px">01</div>

  <div class="step" style="left:865px;top:570px">05</div>
  <div class="step-text" style="left:988px;top:576px;width:196px"><h4>RENEW</h4><p>Seamless policy renewals with transparent pricing based on demonstrated risk improvements</p></div>
</section>

<section class="integrations">
  <h2 class="section-title"><b>Seamlessly Integrates With</b><br>Your Tech Stack</h2>
  <div class="tool" style="left:81px">
    <svg width="56" height="56" viewBox="0 0 56 56"><circle cx="28" cy="28" r="28" fill="#a3fca4"/></svg>
    <span>Identity Platforms</span>
  </div>
  <div class="tool" style="left:343px">
    <svg width="56" height="56" viewBox="0 0 56 56"><rect width="56" height="56" fill="#a3fca4"/></svg>
    <span>Developer Platforms</span>
  </div>
  <div class="tool" style="left:604px">
    <svg width="56" height="56" viewBox="0 0 56 56"><polygon points="2,0 56,28 2,56" fill="#a3fca4"/></svg>
    <span>Endpoint Security</span>
  </div>
  <div class="tool" style="left:865px">
    <svg width="56" height="56" viewBox="0 0 56 56"><polygon points="14,2 42,2 56,28 42,54 14,54 0,28" fill="#a3fca4"/></svg>
    <span>Cloud Infrastructure</span>
  </div>
</section>

<footer class="footer">
  <ul class="footer-nav">
    <li><a href="#">Home</a></li>
    <li><a href="#">Platform</a></li>
    <li><a href="#">Cyber Risk</a></li>
    <li><a href="#">AI Risk</a></li>
    <li><a href="#">Company</a></li>
  </ul>
  <div class="rule" style="top:112px"></div>
  <div class="contact" style="left:160px">
    <div class="contact-icon"><svg width="14" height="18" viewBox="0 0 14 18"><path d="M7 0a7 7 0 0 1 7 7c0 5-7 11-7 11S0 12 0 7a7 7 0 0 1 7-7z" fill="#a3fca4"/><circle cx="7" cy="7" r="2.5" fill="#333"/></svg></div>
    <div><small>Address</small><strong>Lorem ipsum dolor sit<br>consectetur</strong></div>
  </div>
  <div class="contact" style="left:496px">
    <div class="contact-icon"><svg width="16" height="16" viewBox="0 0 16 16"><path d="M3 1l3 3-2 2c1 2 3 4 5 5l2-2 3 3-2 3C7 15 1 9 1 3z" fill="#a3fca4"/></svg></div>
    <div><small>Phone</small><strong>+1 888 888 8888</strong></div>
  </div>
  <div class="contact" style="left:768px">
    <div class="contact-icon"><svg width="18" height="14" viewBox="0 0 18 14"><rect width="18" height="14" rx="2" fill="#a3fca4"/><path d="M1 2l8 6 8-6" stroke="#333" stroke-width="1.6" fill="none"/></svg></div>
    <div><small>Email</small><strong>info@companyname.com</strong></div>
  </div>
  <div class="rule" style="top:222px"></div>
  <p class="copyright">© Copyrights 2026 | All Rights Reserved</p>
</footer>

</body>
</html>
```